Offer banner redesign / Simplifying existing banner

We have a banner there customer can click on to get an offer. We want to simplify this banner and to get it to at minimum. We are not clear about how it shoulderstand look like, but the actual banner you can see here (It's at the top of the page): https://kaminwerk-vorhof.de/rauchrohr-stahl/ We want to get rid of the icons and to reduce the size of the baner. The baner shoulderstand contain the Following text: Affordable chimney using installation service button text: Request free quote

Target Market(s)

Customers from age of 40yrs.

Requirements
Must have
• Clear and good visible button
Nice to have
• It Should be simple and striking.

```html
<!DOCTYPE html>
<html lang="de">
<head>
<meta charset="utf-8">
<title>Kaminwerk Vorhof – Schornsteinangebot</title>
<link rel="stylesheet" href="https://fonts.googleapis.com/css2?family=Fira+Sans:wght@400;500&family=Dosis:wght@300;400;500;600&display=swap">
<style>
:root{
  --orange:#f9b233;
  --orange-soft:#fde7bd;
  --ink:#333;
  --muted:#666;
  --line:#e3e3e3;
  --band:#4a4a4a;
  --white:#fff;
}
*{box-sizing:border-box;margin:0;padding:0}
html,body{width:1200px;height:834px;overflow:hidden;background:var(--white)}
body{position:relative;font-family:"Dosis",sans-serif;color:var(--ink)}
.abs{position:absolute}

.topbar{left:0;top:0;width:1200px;height:50px;border-bottom:1px solid var(--line)}
.brand{left:139px;top:9px;display:flex;align-items:center;gap:8px;font-family:"Fira Sans",sans-serif;font-weight:500;font-size:17px;color:var(--ink);line-height:1}
.brand-dot{width:28px;height:28px;border-radius:50%;background:var(--orange)}
.hotline{right:144px;top:14px;text-align:right}
.hotline-number{display:flex;align-items:center;justify-content:flex-end;gap:6px;font-family:"Fira Sans",sans-serif;font-weight:500;font-size:17px;color:var(--orange);line-height:1}
.hotline-hours{font-size:9px;color:var(--ink);margin-top:4px}

.subbar{left:0;top:51px;width:1200px;height:42px;border-bottom:3px solid var(--line)}
.back-link{left:138px;top:13px;font-size:13px;font-weight:500;color:var(--ink)}
.rating{right:144px;top:6px;display:flex;align-items:center;gap:12px}
.rating-badge{width:28px;height:28px;border-radius:50%;background:#2b2b2b}
.rating-label{font-size:8px;color:#999}
.stars{color:var(--orange);font-size:11px;letter-spacing:1px}
.rating-score{font-size:8px;font-weight:600;line-height:1.2}
.rating-score b{font-size:12px;font-weight:600}

.hero{left:0;top:95px;width:1200px;height:131px;background:linear-gradient(115deg,#3f3f3f 0%,#555 35%,#444 60%,#5a5a5a 85%,#474747 100%)}
.hero-title{left:218px;top:24px;font-family:"Fira Sans",sans-serif;font-weight:500;font-size:42px;color:var(--orange);line-height:1}
.hero-sub{left:218px;top:70px;font-family:"Fira Sans",sans-serif;font-size:24px;color:var(--white);line-height:1}
.hero-cta{left:690px;top:40px;width:306px;height:54px;background:var(--orange);color:var(--white);font-family:"Fira Sans",sans-serif;font-weight:500;font-size:20px;display:flex;align-items:center;justify-content:center;letter-spacing:-.3px}

.section-title{left:373px;top:258px;font-family:"Fira Sans",sans-serif;font-size:26px;color:var(--orange)}
.step{left:373px;top:298px;display:flex;align-items:center;gap:7px;font-size:14px;font-weight:500}
.step-num{width:19px;height:19px;border-radius:50%;background:var(--orange);color:var(--white);font-size:12px;display:flex;align-items:center;justify-content:center}

.benefits{left:139px;top:350px;width:210px;height:254px;border:1px solid var(--line)}
.benefits-head{height:42px;background:var(--orange);color:var(--white);font-family:"Fira Sans",sans-serif;font-weight:500;font-size:15px;padding:12px 11px}
.benefits ul{list-style:none;padding:14px 0 0 15px}
.benefits li{display:flex;gap:6px;font-size:11.5px;line-height:20px;margin-bottom:0}
.benefits li svg{flex:none;margin-top:2px}
.benefits p{font-size:11.5px;line-height:20px;padding:8px 15px 0}

.variant{top:351px;width:210px;height:309px}
.variant.active{border:2px solid var(--line)}
.variant.dim{opacity:.35}
.toggle{left:7px;top:7px;width:36px;height:20px;border-radius:10px;border:2px solid #ccc;background:var(--white)}
.toggle::after{content:"";position:absolute;left:2px;top:2px;width:12px;height:12px;border-radius:50%;background:#ccc}
.active .toggle{border-color:var(--orange)}
.active .toggle::after{left:18px;background:var(--orange)}
.figure{left:40px;top:6px;width:130px;height:255px;background:linear-gradient(180deg,#b9b9b9,#9a6a55 55%,#707070)}
.dim .figure{background:linear-gradient(180deg,#ddd,#cbbdb5 55%,#ddd)}
.pill{top:266px;height:33px;border-radius:17px;background:var(--orange);color:var(--white);font-weight:600;font-size:13px;display:flex;align-items:center;justify-content:center}
.dim .pill{background:var(--orange-soft)}

.field-label{left:373px;top:695px;font-size:12px;color:var(--orange)}
.select{left:373px;top:713px;width:330px;height:27px;border:1px solid #ccc;font-size:10.5px;padding:7px 13px;color:var(--muted)}
.select::after{content:"▾";position:absolute;right:6px;top:6px;font-size:10px;color:var(--ink)}
.hint{left:727px;top:712px;width:330px;height:118px;border:1px solid var(--orange);padding:10px 9px;font-size:12px;line-height:20px;color:#444}
</style>
</head>
<body>

<header class="topbar abs">
  <div class="brand abs"><span class="brand-dot"></span>Kaminwerk Vorhof</div>
  <div class="hotline abs">
    <div class="hotline-number">
      <svg width="16" height="16" viewBox="0 0 16 16"><path d="M3 1l3 3-2 2c1 2 3 4 5 5l2-2 3 3-2 3C6 15 1 10 1 3z" fill="#f9b233"/></svg>
      04521 / 387 1190
    </div>
    <div class="hotline-hours">Mo. - Fr. von 10:00 bis 18:00 Uhr</div>
  </div>
</header>

<nav class="subbar abs">
  <div class="back-link abs">‹ zurück zum Shop</div>
  <div class="rating abs">
    <span class="rating-badge"></span>
    <div><div class="rating-label">Kundenbewertung</div><div class="stars">★★★★★</div></div>
    <div class="rating-score">sehr gut<br><b>4.55</b>/5.00</div>
  </div>
</nav>

<section class="hero abs">
  <div class="hero-title abs">Preiswerter Schornstein</div>
  <div class="hero-sub abs">Wahlweise mit Montageservice</div>
  <div class="hero-cta abs">Kostenloses Angebot anfordern</div>
</section>

<h1 class="section-title abs">In zwei Schritten zum Schornsteinangebot.</h1>
<div class="step abs"><span class="step-num">1</span>Schornsteinangaben:</div>

<aside class="benefits abs">
  <div class="benefits-head">Ihre Vorteile</div>
  <ul>
    <li><svg width="18" height="18" viewBox="0 0 18 18"><circle cx="9" cy="9" r="9" fill="#f9b233"/><path d="M5 9l3 3 5-6" stroke="#fff" stroke-width="2" fill="none"/></svg>Bestpreis-Angebot in max. 60 Minuten</li>
    <li><svg width="18" height="18" viewBox="0 0 18 18"><circle cx="9" cy="9" r="9" fill="#f9b233"/><path d="M5 9l3 3 5-6" stroke="#fff" stroke-width="2" fill="none"/></svg>Kostenlose Beratung nach Angebotserstellung</li>
    <li><svg width="18" height="18" viewBox="0 0 18 18"><circle cx="9" cy="9" r="9" fill="#f9b233"/><path d="M5 9l3 3 5-6" stroke="#fff" stroke-width="2" fill="none"/></svg>Deutsche Markenqualität</li>
  </ul>
  <p>Sie kommen nicht zurecht?<br>Dann rufen Sie uns einfach an:<br>04521 387 119 0</p>
</aside>

<div class="variant active abs" style="left:373px">
  <span class="toggle abs"></span>
  <div class="figure abs" role="img" aria-label="Technische Zeichnung: Standard-Schornstein an der Außenwand"></div>
  <div class="pill abs" style="left:64px;width:100px">Standard</div>
</div>
<div class="variant dim abs" style="left:609px">
  <span class="toggle abs"></span>
  <div class="figure abs" role="img" aria-label="Technische Zeichnung: Schornstein mit Dachdurchführung"></div>
  <div class="pill abs" style="left:40px;width:130px">Dachdurchführung</div>
</div>
<div class="variant dim abs" style="left:845px">
  <span class="toggle abs"></span>
  <div class="figure abs" role="img" aria-label="Technische Zeichnung: Schornstein mit Versatz"></div>
  <div class="pill abs" style="left:69px;width:72px">Versatz</div>
</div>

<label class="field-label abs">Innendurchmesser Schornstein:</label>
<div class="select abs">Innendurchmesser wählen</div>
<div class="hint abs">Der Innendurchmesser des Schornsteins orientiert sich am Rauchrohranschluss der Feuerstätte (Kaminofen, etc.). Falls Sie sich noch nicht für einen Ofen entschieden haben, können Sie hier 150 mm angeben, da das das häufigste Maß ist.</div>

</body>
</html>
```